contemporary upscale hair salon

we need a business card design for a modern upscale salon. I would like the card to be vertical, simple, and easy to read. I would like a black matte finish on the info side with white on the back of the card, white lettering with a splash of red incorporated somewhere in there. I also want to incorporate embossing and/or cut out in the letters. The info I would like; Name of the business (Velora Salon) stylist name (Janet) phone number(4075319264) and web address (www.veloraexample.com) I am open to putting shears on the card but without it looking too cheap. Looking for something really modern and edgy. these are just ideas I have, but feel free to show me your creative ideas.
please note: the website is still under construction please do not use any images or colors off the web page. Also i currently do not have a logo, that will be a future project.

```html
<!DOCTYPE html>
<html lang="en">
<head>
<meta charset="utf-8">
<title>Velora Salon – Business Card</title>
<link rel="stylesheet" href="https://fonts.googleapis.com/css2?family=Questrial&display=swap">
<style>
  :root {
    --backdrop: #1b1819;
    --card-black: #0c0c0d;
    --card-black-glow: #2a2a2c;
    --card-white: #ffffff;
    --ink: #111111;
    --wordmark-light: #d6d6d8;
    --watermark: #ececec;
  }
  * { margin: 0; padding: 0; box-sizing: border-box; }
  html, body {
    width: 1200px;
    height: 1040px;
    overflow: hidden;
    background: var(--backdrop);
    font-family: "Questrial", "Century Gothic", sans-serif;
  }
  .card-set {
    position: relative;
    width: 1200px;
    height: 1040px;
  }
  .card {
    position: absolute;
    top: 135px;
    width: 440px;
    height: 770px;
    overflow: hidden;
  }
  .card--front {
    left: 150px;
    background: radial-gradient(ellipse 70% 45% at 50% 45%, var(--card-black-glow) 0%, var(--card-black) 75%);
  }
  .card--back {
    left: 610px;
    background: var(--card-white);
  }
  .wordmark {
    position: absolute;
    left: 0;
    right: 0;
    top: 245px;
    text-align: center;
    color: var(--wordmark-light);
  }
  .wordmark__name {
    display: block;
    font-size: 92px;
    line-height: 1;
    letter-spacing: 1px;
  }
  .wordmark__sub {
    display: block;
    margin-top: 4px;
    font-size: 20px;
    letter-spacing: 14px;
    padding-left: 90px;
  }
  .watermark {
    position: absolute;
    top: 40px;
    left: 470px;
    transform-origin: top left;
    transform: rotate(90deg);
    color: var(--watermark);
    white-space: nowrap;
  }
  .watermark__name {
    display: block;
    font-size: 150px;
    line-height: 1;
  }
  .watermark__sub {
    display: block;
    font-size: 40px;
    letter-spacing: 32px;
    padding-left: 210px;
  }
  .contact {
    position: absolute;
    left: 0;
    right: 0;
    top: 150px;
    color: var(--ink);
    text-align: center;
  }
  .contact__name {
    display: block;
    font-size: 27px;
    margin-bottom: 38px;
    padding-right: 40px;
  }
  .contact__phone,
  .contact__web {
    display: block;
    font-size: 26px;
    letter-spacing: 1px;
    line-height: 1.35;
  }
</style>
</head>
<body>
  <main class="card-set">
    <section class="card card--front" aria-label="Card front">
      <h1 class="wordmark">
        <span class="wordmark__name">Velora</span>
        <span class="wordmark__sub">Salon</span>
      </h1>
    </section>

    <section class="card card--back" aria-label="Card back">
      <div class="watermark" aria-hidden="true">
        <span class="watermark__name">Velora</span>
        <span class="watermark__sub">Salon</span>
      </div>
      <div class="contact">
        <span class="contact__name">Janet</span>
        <span class="contact__phone">4075319264</span>
        <span class="contact__web">www.veloraexample.com</span>
      </div>
    </section>
  </main>
</body>
</html>
```